Concept packaging of insecticide products

I need a design on my pakaging for my insecticide Zelto Mat product company
It's a new project the background color is blue like the mark finish the design like the mark of Italian Zelto I don't like the red on the background only on the letters not too much the yellow of course on the letters
Updates

pakaging design for insecticide product Tovarin

Target Market(s)

Mosquito repellent insecticide

Industry/Entity Type

Insecticide

Font styles to use
Sans Serif

Colors
0094D4
00A9DD
6FCCEA
C7EBF8
E9F6FB
FFF300
FFF600
FEFA6F
FFFEC7
FFFEE8
EB3D1F
EC4F4E
F09395
F8D3D4
FCEDEE
A7469A
B969AE
D3A5CF
EDDBEB
F8F0F9

Requirements
Must have
• Packaging design
Nice to have
• the blue

```html
<!DOCTYPE html>
<html lang="fr">
<head>
<meta charset="utf-8">
<title>Zelto Mat – emballage</title>
<link rel="stylesheet" href="https://fonts.googleapis.com/css2?family=Poppins:wght@400;500;600;700;800&family=Cairo:wght@400;600;700&display=swap">
<style>
:root{
  --bg:#e4e5e7;
  --navy:#1e2f8f;
  --blue-top:#1f3ea6;
  --blue-mid:#1c63c4;
  --blue-low:#3aa7e6;
  --sky:#6fccea;
  --pale:#c7ebf8;
  --white:#ffffff;
  --yellow:#fff300;
  --red:#eb3d1f;
  --pill-red:#d92b1f;
}
*{margin:0;padding:0;box-sizing:border-box}
html,body{width:1200px;height:900px;overflow:hidden;background:var(--bg)}
body{position:relative;font-family:"Poppins",sans-serif;color:var(--white)}
.panel{position:absolute;top:170px;width:270px;height:560px;
  background:linear-gradient(180deg,var(--blue-top) 0%,var(--blue-mid) 55%,var(--blue-low) 100%);overflow:hidden}
.p1{left:24px}.p2{left:318px}.p3{left:612px}.p4{left:906px}
.brand{position:absolute;top:62px;left:0;right:0;text-align:center;font-weight:800;font-size:54px;letter-spacing:-1px;color:var(--white);line-height:1}
.brand-dot{position:absolute;top:40px;left:40px;width:16px;height:16px;border-radius:50%;background:var(--red)}
.feature{position:absolute;display:flex;align-items:center;gap:6px;font-size:8.5px;line-height:1.15;font-weight:500}
.icon{width:30px;height:30px;border-radius:50%;flex:none}
.icon-ban{background:var(--white);border:3px solid var(--red)}
.icon-window{background:var(--pale);display:flex;align-items:center;justify-content:center}
.photo-ring{position:absolute;top:178px;width:110px;height:110px}
.band{position:absolute;left:-20px;top:300px;width:320px;height:60px;background:var(--yellow);transform:skewY(8deg);opacity:.9}
.pastille{position:absolute;left:18px;top:285px;width:210px;height:120px;border-radius:18px;
  background:linear-gradient(180deg,#8ec8f0,#5aa7e0);transform:rotate(-6deg)}
.clock{position:absolute;top:430px;width:44px;height:60px;text-align:center;font-weight:700;font-size:13px}
.pill{position:absolute;left:20px;right:54px;bottom:20px;height:20px;border-radius:10px;background:var(--white);
  color:var(--pill-red);font-weight:700;font-size:10px;display:flex;align-items:center;justify-content:center}
.p3 .pill{left:34px;right:34px;height:24px;border-radius:12px;font-family:"Cairo",sans-serif;font-size:14px;font-weight:600}
/* back panels */
.back{padding:22px 18px 0}
.back h2{text-align:center;font-weight:600;font-size:15px;margin-bottom:10px}
.steps{list-style:none;font-size:10px;line-height:1.3}
.steps li{display:flex;gap:6px;margin-bottom:6px}
.num{flex:none;width:13px;height:13px;border:1px solid var(--white);border-radius:50%;font-size:8px;font-weight:700;display:flex;align-items:center;justify-content:center;margin-top:1px}
.composition{font-size:10px;text-align:center;margin:2px 0 14px}
.caution{display:flex;align-items:center;gap:8px;font-size:10px;margin-bottom:8px;padding-left:4px}
.caution .icon{width:32px;height:32px}
.icon-hands{background:var(--pale);border:2px solid var(--white)}
.maker{margin-top:30px;text-align:right;font-size:9.5px;line-height:1.35}
.maker p{margin-bottom:8px}
.rtl{direction:rtl;font-family:"Cairo",sans-serif}
.rtl h2{font-family:"Cairo",sans-serif;font-weight:700;font-size:16px}
.rtl .steps{font-size:10px}
.meta{font-size:9px;margin-top:30px;display:grid;grid-template-columns:1fr 1fr;row-gap:14px}
</style>
</head>
<body>

<!-- Face avant (français) -->
<section class="panel p1">
  <span class="brand-dot"></span>
  <div class="brand">Zelto Mat</div>
  <div class="feature" style="left:14px;top:190px"><span class="icon icon-ban"></span>Lutte contre les<br>moustiques et les<br>moustiques tigre</div>
  <div class="feature" style="left:14px;top:232px">
    <span class="icon icon-window"><svg width="16" height="16" viewBox="0 0 16 16"><rect x="2" y="2" width="12" height="12" fill="none" stroke="#1e2f8f" stroke-width="1.6"/><line x1="8" y1="2" x2="8" y2="14" stroke="#1e2f8f" stroke-width="1.6"/></svg></span>
    efficacité<br>fenêtres ouvertes</div>
  <svg class="photo-ring" style="left:150px" viewBox="0 0 110 110">
    <defs><path id="ringFr" d="M55,55 m-46,0 a46,46 0 1,1 92,0 a46,46 0 1,1 -92,0"/></defs>
    <text fill="#ffffff" font-family="Poppins,sans-serif" font-size="6.4" font-weight="600"><textPath href="#ringFr">ASSUREZ-VOUS UNE NUIT PAISIBLE ET PROTÉGEZ VOTRE MAISON DES MOUSTIQUES.</textPath></text>
    <circle cx="55" cy="55" r="34" fill="#9fd3f2" stroke="#ffffff" stroke-width="3" role="img" aria-label="Photo d'un enfant qui dort paisiblement"/>
  </svg>
  <div class="band"></div>
  <div class="pastille" role="img" aria-label="Pile de pastilles anti-moustique bleues"></div>
  <div class="clock" style="right:50px">
    <svg width="40" height="40" viewBox="0 0 40 40"><circle cx="20" cy="20" r="17" fill="none" stroke="#fff" stroke-width="2" stroke-dasharray="3 2"/><circle cx="20" cy="20" r="12" fill="#1e2f8f" stroke="#fff" stroke-width="1.5"/><path d="M20 13v7h5" stroke="#fff" stroke-width="2" fill="none"/></svg>
    10<sup style="font-size:7px">+</sup>H
  </div>
  <div class="pill">30 PASTILLE ANTI-MOUSTIQUE</div>
</section>

<!-- Face arrière (français) -->
<section class="panel p2 back">
  <h2>MODE D'EMPLOI</h2>
  <ol class="steps">
    <li><span class="num">1</span><span>Insérer la pastille <b>Zelto Mat</b> à l'intérieur du diffuseur.</span></li>
    <li><span class="num">2</span><span>Brancher le diffuseur en position horizontale à une prise de courant 220v.</span></li>
    <li><span class="num">3</span><span>Apparition d'une lumière rouge sur l'appareil et diffusion d'une senteur parfumée.</span></li>
    <li><span class="num">4</span><span>La durée de l'efficacité de la pastille <b>Zelto Mat</b> est d'environ dix heures.</span></li>
  </ol>
  <h2 style="margin-top:14px">COMPOSITION</h2>
  <p class="composition">Prallethrine, neperfluthrine, solvant, colorant, parfum</p>
  <h2>PRECAUTION D'EMPLOI</h2>
  <div class="caution"><span class="icon icon-ban"></span>Ne pas laisser à la<br>portée des enfants.</div>
  <div class="caution"><span class="icon icon-hands"></span>Laver les mains après<br>chaque usage.</div>
  <div class="maker">
    <p>SARL Zelto société de<br>production insecticide<br>14 Z.A.C EL NOUR SETIFIA</p>
    <p>TELEPHONE:</p>
    <p>EMAIL:</p>
    <p>Marque Déposée</p>
  </div>
</section>

<!-- Face avant (arabe) -->
<section class="panel p3">
  <span class="brand-dot"></span>
  <div class="brand">Zelto Mat</div>
  <div class="feature rtl" style="left:14px;top:190px;direction:ltr"><span class="icon icon-ban"></span><span class="rtl">مكافحة البعوض<br>والبعوض النمر</span></div>
  <div class="feature" style="left:14px;top:232px">
    <span class="icon icon-window"><svg width="16" height="16" viewBox="0 0 16 16"><rect x="2" y="2" width="12" height="12" fill="none" stroke="#1e2f8f" stroke-width="1.6"/><line x1="8" y1="2" x2="8" y2="14" stroke="#1e2f8f" stroke-width="1.6"/></svg></span>
    <span class="rtl">فعالة والنوافذ<br>مفتوحة</span></div>
  <svg class="photo-ring" style="left:148px" viewBox="0 0 110 110">
    <defs><path id="ringAr" d="M55,55 m-46,0 a46,46 0 1,1 92,0 a46,46 0 1,1 -92,0"/></defs>
    <text fill="#ffffff" font-family="Cairo,sans-serif" font-size="9" font-weight="600"><textPath href="#ringAr">نوم هادئ لك وحماية منزلك من البعوض</textPath></text>
    <circle cx="55" cy="55" r="34" fill="#9fd3f2" stroke="#ffffff" stroke-width="3" role="img" aria-label="Photo d'un enfant qui dort paisiblement"/>
  </svg>
  <div class="band"></div>
  <div class="pastille" role="img" aria-label="Pile de pastilles anti-moustique bleues"></div>
  <div class="clock" style="left:28px">
    <svg width="40" height="40" viewBox="0 0 40 40"><circle cx="20" cy="20" r="17" fill="none" stroke="#fff" stroke-width="2" stroke-dasharray="3 2"/><circle cx="20" cy="20" r="12" fill="#1e2f8f" stroke="#fff" stroke-width="1.5"/><path d="M20 13v7h5" stroke="#fff" stroke-width="2" fill="none"/></svg>
    10<sup style="font-size:7px">+</sup>H
  </div>
  <div class="pill" dir="rtl">30 قرص مضاد للبعوض</div>
</section>

<!-- Face arrière (arabe) -->
<section class="panel p4 back rtl">
  <h2>كيفية الإستعمال</h2>
  <ol class="steps">
    <li><span class="num">1</span><span>أدخل قرص Zelto Mat في جهاز النشر</span></li>
    <li><span class="num">2</span><span>صل الجهاز أفقيا بمأخذ كهربائي 220V</span></li>
    <li><span class="num">3</span><span>ظهور ضوء أحمر على الجهاز وإنتشار رائحة لطيفة</span></li>
  </ol>
  <h2 style="margin-top:26px">المكونات</h2>
  <p class="composition">براليترين، نيبرفلوترين، مذيب، ملون، عطر</p>
  <h2 style="margin-top:18px">إحتياطات الإستعمال</h2>
  <div class="caution"><span class="icon icon-ban"></span>لايترك في متناول الأطفال.</div>
  <div class="caution"><span class="icon icon-hands"></span>غسل الأيدي بعد الإستعمال.</div>
  <div class="meta">
    <span>الهاتف</span><span></span>
    <span>الفاكس</span><span></span>
    <span>مقرر رقم:</span><span>بتاريخ</span>
    <span>علامة مسجلة</span><span></span>
    <span>تاريخ الإنتاج:</span><span>نهاية الإنتاج</span>
  </div>
</section>

</body>
</html>
```